Young Accounting firm needing a captivating business card

We need a business card design that forces the person to look at the card because its either gold foil, plastic, or lettering pop up etc. We already have a logo with a specific gold color and we need to make it pop. We are an accounting firm. I need the words" accounting, payroll, licenses, audits, taxes" somewhere on the business card so as to describe what we do- preferably on the side where the logo is at.

Industry/Entity Type

Accounting

Contact Information for Business Card

Address 48276 9th Ave S Ste 305, Federal Way, WA 98117
Business Phone (360)418-2096
Fax (360)418-2157
Office Cell Phone (360)586-7319

Font styles to use
Serif

Colors
85abd2

Requirements
Must have
• It should state
• "Accounting" "Taxes" "Audits" "Licenses" "Payroll"
Nice to have
• Matte with gold foil, different textures, With Either a textured ivory background or gray blue slate background
Should not have
• colorful colors

```html
<!DOCTYPE html>
<html lang="en">
<head>
<meta charset="utf-8">
<title>Hartwell Ledger – Business Card</title>
<link href="https://fonts.googleapis.com/css2?family=EB+Garamond:wght@400;500;600&family=Cinzel:wght@500&display=swap" rel="stylesheet">
<style>
  :root {
    --backdrop: #8a8b8d;
    --card: #141414;
    --card-edge: #0b0b0b;
    --gold: #c9a13e;
    --gold-light: #e6c866;
    --ink-light: #f2efe8;
  }
  * { margin: 0; padding: 0; box-sizing: border-box; }
  html, body {
    width: 1171px; height: 1200px; overflow: hidden;
    background: var(--backdrop);
  }
  .stage {
    position: relative; width: 1171px; height: 1200px;
    display: flex; flex-direction: column; align-items: center; justify-content: center; gap: 54px;
  }
  .card {
    position: relative; width: 880px; height: 503px;
    background: var(--card);
    border: 1px solid var(--card-edge);
    box-shadow: 0 18px 40px rgba(0,0,0,.35);
    font-family: "EB Garamond", Georgia, serif;
  }

  /* Front */
  .card-front .brand {
    position: absolute; left: 0; right: 0; top: 150px;
    display: flex; align-items: center; justify-content: center; gap: 20px;
  }
  .brand-square { width: 46px; height: 46px; background: var(--gold); flex: none; }
  .brand-name {
    font-family: "EB Garamond", Georgia, serif; font-weight: 500;
    color: var(--gold); font-size: 60px; line-height: 1; letter-spacing: .5px;
  }
  .services {
    position: absolute; left: 0; right: 0; top: 392px;
    text-align: center; color: var(--ink-light); font-size: 24px; letter-spacing: .5px;
  }
  .services .divider { color: var(--gold); margin: 0 12px; }

  /* Back */
  .card-back .brand {
    position: absolute; left: 40px; width: 350px; top: 222px;
    display: flex; align-items: center; justify-content: center; gap: 14px;
  }
  .card-back .brand-square { width: 34px; height: 34px; }
  .card-back .brand-name { font-size: 44px; }
  .rule {
    position: absolute; left: 415px; top: 120px; width: 2px; height: 300px; background: var(--gold);
  }
  .contact { position: absolute; left: 448px; top: 86px; color: var(--ink-light); }
  .person-name {
    font-family: "Cinzel", "Times New Roman", serif; font-weight: 500;
    color: var(--gold-light); font-size: 34px; letter-spacing: 1px; line-height: 1.1;
  }
  .person-title { font-size: 22px; margin-top: 4px; }
  .address { font-size: 22px; line-height: 1.3; margin-top: 14px; }
  .lines { list-style: none; margin-top: 14px; font-size: 22px; line-height: 1.3; }
  .lines li { display: flex; align-items: center; gap: 14px; }
  .lines svg { width: 16px; height: 16px; flex: none; }
</style>
</head>
<body>
<main class="stage">

  <section class="card card-front" aria-label="Card front">
    <div class="brand">
      <span class="brand-square"></span>
      <span class="brand-name">Hartwell Ledger</span>
    </div>
    <p class="services">Accounting<span class="divider">|</span>Taxes<span class="divider">|</span>Audits<span class="divider">|</span>Licenses<span class="divider">|</span>Payroll</p>
  </section>

  <section class="card card-back" aria-label="Card back">
    <div class="brand">
      <span class="brand-square"></span>
      <span class="brand-name">Hartwell Ledger</span>
    </div>
    <div class="rule"></div>
    <div class="contact">
      <h1 class="person-name">MARTIN HALE</h1>
      <p class="person-title">Owner</p>
      <p class="address">48276 9th Ave S Ste 305,<br>Federal Way, WA 98117</p>
      <ul class="lines">
        <li>
          <svg viewBox="0 0 16 16" aria-hidden="true"><path fill="#c9a13e" d="M3.6 1.5l2.3 2.6-1.3 1.7c.9 2 2.4 3.5 4.4 4.4l1.7-1.3 2.6 2.3-1.4 2.2C6.8 13.3 2.7 9.2 1.4 3z"/></svg>
          (360)418-2096
        </li>
        <li>
          <svg viewBox="0 0 16 16" aria-hidden="true"><rect x="4" y="1" width="8" height="14" rx="1.5" fill="none" stroke="#c9a13e" stroke-width="1.6"/><circle cx="8" cy="12.5" r=".9" fill="#c9a13e"/></svg>
          (360)586-7319
        </li>
        <li>
          <svg viewBox="0 0 16 16" aria-hidden="true"><rect x="4" y="1.5" width="8" height="4" fill="none" stroke="#c9a13e" stroke-width="1.4"/><rect x="1.5" y="6" width="13" height="6.5" rx="1" fill="#c9a13e"/><rect x="4" y="11" width="8" height="3.5" fill="#141414" stroke="#c9a13e" stroke-width="1.2"/></svg>
          (360)418-2157
        </li>
        <li>
          <svg viewBox="0 0 16 16" aria-hidden="true"><rect x="1.5" y="3.5" width="13" height="9" fill="none" stroke="#c9a13e" stroke-width="1.4"/><path d="M1.5 3.5L8 9l6.5-5.5" fill="none" stroke="#c9a13e" stroke-width="1.4"/></svg>
          info@martinhale.com
        </li>
      </ul>
    </div>
  </section>

</main>
</body>
</html>
```